Feral Horizon, a 3d voxel survival video game needs a card for gaming conventions

I am the lead developer for Feral Horizon http://www.FeralHorizon.example and need a business card to hand out at an indie gaming convention
The card would need to include the game name, website url, my name, position (Lead Developer), e-mail and phone number
The game is a 3d, voxel (with smooth terrain) based survival game with guns and wildlife. The main icon of the game would likely be a grizzly bear but I am willing to accept other designs too.
Attached is a media kit for the game with some images you can use but don't have to its just what little art I can provide. Anything on the website or from the video game can also be used. unrelated art can also be used.
Target Market(s)
Indie Developers/publishers at conferences
Industry/Entity Type
Games
Contact Information for Business Card
Name: Corwin Aldersby
Position: Lead Developer
E-mail: Pale_Lanterns@mailbox.example
Phone number: 555-207-3186

```html
<!DOCTYPE html>
<html lang="en">
<head>
<meta charset="utf-8">
<title>Feral Horizon – Business Card</title>
<link rel="stylesheet" href="https://fonts.googleapis.com/css2?family=Open+Sans:wght@400;600;800&display=swap">
<style>
  :root {
    --page-bg: #e8e5e0;
    --front-light: #f4f4f2;
    --front-mist: #d9dad6;
    --back-center: #d6d2b8;
    --back-mid: #6f6c4a;
    --back-edge: #1f1e14;
    --bear-brown: #8a5a34;
    --bear-dark: #5a3820;
    --brand: #b4532c;
    --ink: #1c1c1c;
    --ink-soft: #4a4a4a;
    --url-red: #b23a22;
  }
  * { margin: 0; padding: 0; box-sizing: border-box; }
  html, body {
    width: 1200px; height: 780px; overflow: hidden;
    background: var(--page-bg);
    font-family: "Open Sans", sans-serif;
  }
  .canvas {
    width: 1200px; height: 780px;
    display: flex; align-items: center; justify-content: center; gap: 40px;
  }
  .card {
    position: relative;
    width: 540px; height: 309px;
    overflow: hidden;
    box-shadow: 0 6px 18px rgba(0,0,0,.22);
  }
  .brand-name {
    position: absolute;
    font-weight: 800; font-size: 30px; line-height: 1.05;
    color: var(--brand); text-transform: uppercase; letter-spacing: 1px;
    white-space: nowrap;
  }

  /* Front */
  .card--front {
    background: linear-gradient(160deg, var(--front-light) 0%, var(--front-mist) 55%, var(--front-light) 100%);
  }
  .front__scenery {
    position: absolute; inset: 0;
    background: radial-gradient(ellipse 70% 50% at 55% 20%, rgba(160,165,155,.35), transparent 70%),
                radial-gradient(ellipse 40% 30% at 30% 55%, rgba(150,150,145,.25), transparent 70%);
  }
  .front__bear {
    position: absolute; left: 24px; top: 118px;
    width: 90px; height: 108px; border-radius: 46% 46% 30% 30%;
    background: radial-gradient(circle at 50% 40%, var(--bear-brown), var(--bear-dark));
  }
  .front__brand { left: 122px; top: 138px; }
  .front__contact {
    position: absolute; left: 302px; top: 118px;
    color: var(--ink);
  }
  .contact__name { font-weight: 600; font-size: 18px; }
  .contact__role { font-size: 12.5px; color: var(--ink-soft); margin-bottom: 8px; }
  .contact__line { display: flex; align-items: center; gap: 7px; font-size: 12px; margin-top: 3px; white-space: nowrap; }
  .contact__icon { width: 13px; height: 13px; flex: none; }

  /* Back */
  .card--back {
    background: radial-gradient(ellipse 65% 70% at 50% 52%, var(--back-center) 0%, var(--back-mid) 55%, var(--back-edge) 100%);
  }
  .back__bear-photo {
    position: absolute; left: 26px; top: 22px;
    width: 240px; height: 140px; border-radius: 40% 48% 22% 30%;
    background: radial-gradient(ellipse at 55% 40%, #a77249, var(--bear-dark) 85%);
  }
  .back__brand { left: 230px; top: 170px; }
  .back__bear-head {
    position: absolute; left: 420px; top: 160px;
    width: 80px; height: 66px; border-radius: 48%;
    background: radial-gradient(circle at 50% 45%, var(--bear-brown), var(--bear-dark));
  }
  .back__url {
    position: absolute; left: 0; right: 0; bottom: 24px; text-align: center;
    font-weight: 600; font-size: 15px; color: var(--url-red);
  }
</style>
</head>
<body>
<main class="canvas">
  <section class="card card--front">
    <div class="front__scenery" role="img" aria-label="Misty forest and mountain landscape"></div>
    <div class="front__bear" role="img" aria-label="Roaring grizzly bear photograph"></div>
    <div class="brand-name front__brand">Feral<br>Horizon</div>
    <div class="front__contact">
      <p class="contact__name">Corwin Aldersby</p>
      <p class="contact__role">Lead Developer</p>
      <p class="contact__line">
        <svg class="contact__icon" viewBox="0 0 16 16"><rect width="16" height="16" rx="2" fill="#1c1c1c"/><path d="M5 3.5l2 2-1.2 1.4a7 7 0 0 0 3.3 3.3L10.5 9l2 2-1.3 1.6C7.5 12.4 3.6 8.5 3.4 4.8z" fill="#fff"/></svg>
        555-207-3186
      </p>
      <p class="contact__line">
        <svg class="contact__icon" viewBox="0 0 16 16"><rect width="16" height="16" rx="2" fill="#1c1c1c"/><rect x="3" y="4.5" width="10" height="7" fill="none" stroke="#fff" stroke-width="1.2"/><path d="M3 4.5l5 4 5-4" fill="none" stroke="#fff" stroke-width="1.2"/></svg>
        Pale_Lanterns@mailbox.example
      </p>
    </div>
  </section>

  <section class="card card--back">
    <div class="back__bear-photo" role="img" aria-label="Grizzly bear standing on a rock"></div>
    <div class="brand-name back__brand">Feral<br>Horizon</div>
    <div class="back__bear-head" role="img" aria-label="Roaring grizzly bear head"></div>
    <p class="back__url">www.feralhorizon.example</p>
  </section>
</main>
</body>
</html>
```